3 x DIN A4 Flyer, Vorder- und Rückseite
Zielgruppe
Handwerksunternehmen
Aufgabenstellung
Wir benötigen 3 Werbeflyer die in Zeitschriften beigelegt werden. Jeweils DIN A4, Vorderseite beschreibt das Produkt, Rückseite kann zur Bestellung mittels Faxantwort benutzt werden. Profibilder und Text wird vollständig geliefert.

```html
<!DOCTYPE html>
<html lang="de">
<head>
<meta charset="utf-8">
<title>Baustellen-Handy mit Solar-Betrieb</title>
<link href="https://fonts.googleapis.com/css2?family=Arimo:wght@400;700&family=Titan+One&display=swap" rel="stylesheet">
<style>
  :root {
    --paper: #ffffff;
    --ink: #1a1a1a;
    --title-blue: #2f5fd0;
    --title-edge: #0c1f5c;
    --label-yellow: #f6d21a;
    --label-edge: #3a2f00;
    --pebble-light: #e9e5df;
    --pebble-mid: #c9c2b8;
    --pebble-dark: #9d968c;
  }
  html, body { margin: 0; padding: 0; overflow: hidden; background: var(--paper); }
  .flyer {
    position: relative; width: 848px; height: 1200px; overflow: hidden;
    background: var(--paper); color: var(--ink);
    font-family: "Arimo", Arial, sans-serif;
  }
  .product-photo {
    position: absolute; left: 0; top: 560px; width: 848px; height: 640px;
    background:
      radial-gradient(ellipse 200px 240px at 500px 330px, rgba(246,210,26,.45), rgba(246,210,26,0) 70%),
      linear-gradient(180deg, rgba(255,255,255,1) 0%, rgba(233,229,223,.7) 20%, var(--pebble-mid) 60%, var(--pebble-dark) 100%);
    opacity: .55;
  }
  .headline {
    position: absolute; top: 26px; left: 0; width: 848px; margin: 0; text-align: center;
    font-family: "Titan One", "Arial Black", sans-serif; font-weight: 400;
    font-size: 36px; letter-spacing: 1px; color: var(--title-blue);
    -webkit-text-stroke: 1.5px var(--title-edge);
  }
  .intro {
    position: absolute; top: 104px; left: 112px; width: 666px;
    font-size: 15px; line-height: 19px;
  }
  .intro p { margin: 0 0 17px; }
  .intro h2 { font-size: 15px; line-height: 19px; margin: 0; font-weight: 700; }
  .features {
    position: absolute; top: 0; left: 62px; width: 730px; height: 1200px;
    margin: 0; padding: 0; list-style: none; font-size: 15px; line-height: 19px;
  }
  .feature { position: absolute; left: 0; width: 730px; display: flex; }
  .feature-label {
    width: 143px; flex: none; font-weight: 700; color: var(--label-yellow);
    -webkit-text-stroke: .5px var(--label-edge);
    text-shadow: 0 0 1px var(--label-edge);
  }
  .feature-label::before { content: "• "; }
  .feature-value { flex: 1; }
  .feature-price .feature-value { font-weight: 700; }
  .legal {
    position: absolute; top: 1098px; left: 207px; width: 440px;
    font-size: 11px; line-height: 14px; margin: 0;
  }
  .publisher {
    position: absolute; top: 1027px; left: 666px; width: 160px;
    font-size: 10.5px; line-height: 13px;
  }
  .publisher p { margin: 0 0 12px; }
  .publisher-name { font-weight: 700; }
</style>
</head>
<body>
<div class="flyer">
  <div class="product-photo" role="img" aria-label="Gelbes Baustellen-Handy mit Schutzhülle liegt auf Kieselsteinen"></div>

  <h1 class="headline">Baustellen-Handy mit Solar-Betrieb</h1>

  <div class="intro">
    <p>Übersteht dank <strong>abnehmbarem &amp; nachleuchtendem Protector</strong> Stürze aus 2 Meter</p>
    <p>Das geniale Baustellen-Handy für Handwerker, die <strong>Freiheit</strong> und <strong>Unabhängigkeit</strong> lieben.<br>Die Freiheit, nicht mehr länger auf Ihr Handy aufpassen zu müssen. Und die Unabhängigkeit von einer anderen Stromquelle als der Sonne.</p>
    <p>Dank Schutzklasse IP67 lässt es sich auch von Regen oder kurzzeitigem Untertauchen nicht beeindrucken. Das ideale Handy für alle, die viel im Freien arbeiten oder unterwegs sind, <strong>z.B. auf der Baustelle, in den Bergen, auf dem Boot oder beim Abenteuer-Urlaub.</strong></p>
    <h2>Genießen Sie Unabhängigkeit:</h2>
    <p>Der Akku hat eine Standby-Zeit von über einer Woche. Sobald Ihr RX-410 ans Tageslicht kommt, tankt es über seine Solarzelle neue Energie.</p>
    <h2>Auch genial:</h2>
    <p>Der phosphoreszierende Impact-Protector. Damit geht Ihr neues Action-Handy auch im Dunkeln nicht verloren.</p>
    <h2>Technik pur ohne Schnickschnack:</h2>
    <p>Das RX-410 SOL bietet genau das, was Sie im Alltag brauchen. Bequemes Telefonieren und schnelles SMS-Schreiben.</p>
    <p>Und wenn es in die Zivilisation zurückkehrt, wird das Handy auf Wunsch zum Normalo:<br>Der Protector lässt sich einfach abnehmen.</p>
  </div>

  <ul class="features">
    <li class="feature" style="top:588px"><span class="feature-label">Startklar:</span><span class="feature-value">Vertrags- und SIM-Lock-Frei, sofort bereit für Ihre SIM-Karte</span></li>
    <li class="feature" style="top:620px"><span class="feature-label">Unverwüstlich:</span><span class="feature-value">Stoßfestes sowie staub- und wasserdichtes Gehäuse<br>(Schutzklasse IP67)</span></li>
    <li class="feature" style="top:665px"><span class="feature-label">Unabhängig &amp; umweltfreundlich:</span><span class="feature-value"><br>Integrierte Solarzelle auf der Rückseite</span></li>
    <li class="feature" style="top:718px"><span class="feature-label">Nachtaktiv:</span><span class="feature-value">Phosphoreszierender Impact Protector (Schutz-Case),<br>hintergrund-beleuchtetes Tastenfeld</span></li>
    <li class="feature" style="top:764px"><span class="feature-label">Verwandlungs-künstler:</span><span class="feature-value"><br>Impact Protector aus Hartplastik lässt sich abnehmen</span></li>
    <li class="feature" style="top:812px"><span class="feature-label">Überall praktisch:</span><span class="feature-value">UKW-Radio, LED-Taschenlampe, Spiele, Rechner, Wecker</span></li>
    <li class="feature" style="top:842px"><span class="feature-label">Kontraststark:</span><span class="feature-value">3,6 cm/ 1,8" Farb-TFT-Display, hintergrund-beleuchtet</span></li>
    <li class="feature" style="top:872px"><span class="feature-label">Klangfreudig:</span><span class="feature-value">Polyphone Klingeltöne (16-stimmig), Vibrationsalarm</span></li>
    <li class="feature" style="top:902px"><span class="feature-label">Kontaktfreudig:</span><span class="feature-value">SMS-Messaging, Telefonbuch (100 Einträge)</span></li>
    <li class="feature" style="top:932px"><span class="feature-label">Zuverlässig:</span><span class="feature-value">Li-Ion-Akku 1000 mAh für 200 Min. Sprechen und 200 Std. Standby<br>(lädt per Solar/ Netzteil)</span></li>
    <li class="feature" style="top:978px"><span class="feature-label">Handlich:</span><span class="feature-value">Maße mit Hülle 108 x 48,5 x 18,5 mm</span></li>
    <li class="feature" style="top:1010px"><span class="feature-label">Komplett:</span><span class="feature-value">Inkl. Akku, 230V-Ladegerät,<br>Ohrhörer, deutsches Handbuch</span></li>
    <li class="feature feature-price" style="top:1065px"><span class="feature-label">Preis:</span><span class="feature-value">120,- netto</span></li>
  </ul>

  <p class="legal">Alle angegebenen Preise verstehen sich in Euro zzgl. der gesetzlichen geltenden Mehrwertsteuer von derzeit 19%. Die Lieferung erfolgt ca.10 Tage nach Bestelleingang. <strong>Porto/Verpackung 8,90 Euro</strong></p>

  <div class="publisher">
    <p class="publisher-name">Fördergesellschaft des Klempner- und Lüftungsbaugewerbes mbH</p>
    <p>Lindenhofer Straße 42<br>80331 Musterstadt</p>
    <p>www.klvt.de</p>
  </div>
</div>
</body>
</html>
```